Global Weight loss program

we need a business card based in Brooklyn , NY called PeppertonRUN . Mara Dulvik Tenbrook the founder and creator of PeppertonRUN Movement. A business based around nutrition, health, Whole Foods and fitness.

Industry/Entity Type

Food Service

Contact Information for Business Card

Phone number : 718-555-0143
website www.peppertonrun.com
email : mara@peppertonrun.com

Font styles to use
Sans Serif

Requirements
Must have
• logo colors
• green black and gold
Nice to have
• must be simple and sharp.
Should not have
• pictures of items

```html
<!DOCTYPE html>
<html lang="en">
<head>
<meta charset="utf-8">
<title>PeppertonRUN Business Card</title>
<link rel="stylesheet" href="https://fonts.googleapis.com/css2?family=Open+Sans:wght@400;600&display=swap">
<style>
  :root {
    --page: #d3d3d3;
    --card: #2b2829;
    --white: #ffffff;
    --green: #14a84b;
    --green-dark: #0a9444;
    --green-light: #8fd64c;
    --divider: #1f5a33;
    --muted: #bfbfbf;
  }
  * { margin: 0; padding: 0; box-sizing: border-box; }
  html, body { width: 1200px; height: 1200px; overflow: hidden; }
  body {
    background: var(--page);
    font-family: "Open Sans", Arial, sans-serif;
    display: flex;
    flex-direction: column;
    align-items: center;
    justify-content: center;
    gap: 70px;
  }
  .card {
    position: relative;
    width: 800px;
    height: 457px;
    background: var(--card);
    box-shadow: 0 18px 40px rgba(0,0,0,0.25);
    overflow: hidden;
  }
  .card__band {
    position: absolute;
    left: 0; right: 0; bottom: 0;
    height: 22px;
    background: linear-gradient(90deg, var(--green-light) 0%, var(--green) 45%, var(--green-dark) 100%);
  }
  .brand { display: flex; flex-direction: column; align-items: flex-start; }
  .brand__row { display: flex; align-items: center; gap: 12px; }
  .brand__dot { border-radius: 50%; background: var(--green); flex: none; }
  .brand__name { color: var(--white); font-weight: 400; letter-spacing: 0.5px; line-height: 1; }
  .brand__tagline { color: var(--muted); letter-spacing: 3px; margin-top: 8px; }

  /* brand side */
  .card--front .brand {
    position: absolute; left: 50%; top: 44%;
    transform: translate(-50%, -50%);
    align-items: center;
  }
  .card--front .brand__dot { width: 30px; height: 30px; }
  .card--front .brand__name { font-size: 56px; }
  .card--front .brand__tagline { font-size: 13px; }

  /* contact side */
  .card--back .brand { position: absolute; left: 70px; top: 46px; }
  .card--back .brand__dot { width: 18px; height: 18px; }
  .card--back .brand__name { font-size: 32px; }
  .card--back .brand__tagline { font-size: 9px; letter-spacing: 2px; margin-top: 6px; }

  .person { position: absolute; right: 64px; top: 190px; text-align: right; }
  .person__name { color: var(--green); font-size: 30px; font-weight: 400; }
  .person__role { color: var(--white); font-size: 19px; margin-top: 2px; }

  .contacts {
    position: absolute; left: 60px; right: 50px; bottom: 52px;
    display: flex; align-items: flex-end; justify-content: space-between;
  }
  .contact { flex: none; display: flex; flex-direction: column; align-items: center; gap: 12px; }
  .contact__icon { width: 26px; height: 26px; }
  .contact__text { color: var(--white); font-size: 17px; white-space: nowrap; }
  .contact__divider { flex: none; width: 1px; height: 56px; background: var(--divider); transform: skewX(-30deg); }
</style>
</head>
<body>

  <section class="card card--back" aria-label="Business card, contact side">
    <div class="brand">
      <div class="brand__row">
        <span class="brand__dot"></span>
        <span class="brand__name">PeppertonRUN</span>
      </div>
      <span class="brand__tagline">Food, Movement and Wellness</span>
    </div>

    <div class="person">
      <p class="person__name">Mara Dulvik Tenbrook</p>
      <p class="person__role">Founder</p>
    </div>

    <div class="contacts">
      <div class="contact">
        <svg class="contact__icon" viewBox="0 0 26 26" aria-hidden="true">
          <circle cx="13" cy="13" r="11.5" fill="none" stroke="#14a84b" stroke-width="2"/>
          <path d="M9.5 7.5l2 2.2-1.2 1.6c.8 1.7 2 2.9 3.6 3.7l1.6-1.2 2.2 2-1.3 1.7c-3.8-.6-7-3.8-7.6-7.6z" fill="#14a84b"/>
        </svg>
        <span class="contact__text">718-555-0143</span>
      </div>
      <span class="contact__divider"></span>
      <div class="contact">
        <svg class="contact__icon" viewBox="0 0 26 26" aria-hidden="true">
          <circle cx="13" cy="13" r="11.5" fill="none" stroke="#14a84b" stroke-width="2"/>
          <rect x="7" y="9" width="12" height="8.5" fill="#14a84b"/>
          <path d="M7 9l6 5 6-5" fill="none" stroke="#2b2829" stroke-width="1.4"/>
        </svg>
        <span class="contact__text">mara@peppertonrun.com</span>
      </div>
      <span class="contact__divider"></span>
      <div class="contact">
        <svg class="contact__icon" viewBox="0 0 26 26" aria-hidden="true">
          <circle cx="13" cy="13" r="11.5" fill="none" stroke="#14a84b" stroke-width="2"/>
          <circle cx="13" cy="13" r="6" fill="none" stroke="#14a84b" stroke-width="1.6"/>
          <path d="M7 13h12M13 7c-2.5 3.5-2.5 8.5 0 12M13 7c2.5 3.5 2.5 8.5 0 12" fill="none" stroke="#14a84b" stroke-width="1.2"/>
        </svg>
        <span class="contact__text">www.peppertonrun.com</span>
      </div>
    </div>

    <div class="card__band"></div>
  </section>

  <section class="card card--front" aria-label="Business card, brand side">
    <div class="brand">
      <div class="brand__row">
        <span class="brand__dot"></span>
        <span class="brand__name">PeppertonRUN</span>
      </div>
      <span class="brand__tagline">Food, Movement and Wellness</span>
    </div>
    <div class="card__band"></div>
  </section>

</body>
</html>
```